Wine Label named: Amber Ridge

We are a wine producer, who wishes to launch a new premium wine called: Amber Ridge
Our winery is situated in a rolling hill, with slopes, where Amber Ridge exists in the property. One dates to the 15th century and the other more recent to the 18th century. Its a unique feature of the winery and we wish to create a label that represents these, but is NOT religious! Difficult task I know. Think you can pull it off? Let us see it! We start with one label, but the winner will have 5 more labels to design.

Target Market(s)

30-50 year old men

Industry/Entity Type

Wine

Colors

Designer to choose colors to be used in the design.

Requirements
Must have
• serious look and premium feel. name of the wine: Amber Ridge
Nice to have
• 2019 14% ABV
Should not have
• a religious look and feel

```html
<!DOCTYPE html>
<html lang="en">
<head>
<meta charset="UTF-8">
<title>Amber Ridge – Wine Label</title>
<link rel="stylesheet" href="https://fonts.googleapis.com/css2?family=Montserrat:wght@700;900&display=swap">
<style>
  :root {
    --paper: #ffffff;
    --frame: #4b4b40;
    --label-ground: #231f20;
    --name-primary: #66665a;
    --name-secondary: #4a4a3f;
    --vintage-gold: #b4b07a;
  }
  html, body {
    margin: 0;
    padding: 0;
    width: 1200px;
    height: 1200px;
    overflow: hidden;
    background: var(--paper);
  }
  .label-canvas {
    display: block;
    width: 1200px;
    height: 1200px;
  }
  .label-frame { fill: var(--frame); }
  .label-panel { fill: var(--label-ground); }
  .brand-mark { fill: var(--vintage-gold); }
  .brand-name {
    font-family: "Montserrat", sans-serif;
    font-weight: 700;
    font-size: 30px;
    letter-spacing: 3px;
    fill: var(--vintage-gold);
  }
  .wine-name {
    font-family: "Montserrat", sans-serif;
    font-weight: 900;
  }
  .wine-name--primary { fill: var(--name-primary); }
  .wine-name--secondary { fill: var(--name-secondary); }
  .vintage-line {
    font-family: "Montserrat", sans-serif;
    font-weight: 700;
    font-size: 22px;
    letter-spacing: 1px;
    fill: var(--vintage-gold);
  }
</style>
</head>
<body>
<svg class="label-canvas" viewBox="0 0 1200 1200" xmlns="http://www.w3.org/2000/svg">
  <rect class="label-frame" x="206" y="52" width="788" height="1096"/>
  <rect class="label-panel" x="239" y="90" width="721" height="1020"/>

  <g class="brand-signature">
    <rect class="brand-mark" x="470" y="411" width="26" height="26"/>
    <text class="brand-name" x="512" y="435">AMBER RIDGE</text>
  </g>

  <text class="wine-name wine-name--primary" x="319" y="736" font-size="215"
        textLength="552" lengthAdjust="spacingAndGlyphs">AMBER</text>
  <text class="wine-name wine-name--secondary" x="319" y="837" font-size="115"
        textLength="554" lengthAdjust="spacingAndGlyphs">RIDGE</text>

  <text class="vintage-line" x="598" y="1047" text-anchor="middle">2019 14% ABV</text>
</svg>
</body>
</html>
```